Gardowell - Direct Mail DL flyer design

Create a direct market flyer (d/l size) to compel people to act and visit our website to buy life insurance.

Copy, example images and notes are provided

Target Market(s)

Families with debt who need life insurance

Industry/Entity Type

Insurance

Requirements
Must have
• Our logo
• Colours are Blue C99, M79, Y0, K0 Green C40, M0, Y100, K0
• Copy side 1 is "For the price of a coffee you can ensure you and your family get the right start."
• Copy side 2 is "It doesn't sound like much, but when it comes to life insurance, $1 a day* can make a huge difference if you were to die.
• For the cost of a cup of coffee a day, you can ensure your family will be left with enough to protect the home, pay for ongoing living expenses and fund your children's continued education.
• Your life is important
• Apply today and get 1 month free cover
• Build your tomorrow
• company logo gardowell.com.au make prominant
• *For a monthly premium of $25.33, a 35 year old non-smoking male can obtain $300,000 of term life cover.
• Example for illistration purpose only. The premium cited is current as at February 2016, is based on the factors referred to in the example and subject to underwriting. You should consider whether this product is appropriate for you. Refer to the Product Disclosure Statement, available from gardowell before deciding whether to acquire the product."
• Footer
• Gardowell Pty Ltd
• ABN 47 253 918 604 AFS Licence 729140
Nice to have
• Coffee cup with pods/capsuals around it white background side 1 and coffee ring stain on reverse as watermark
• Trusafe has been awarded - Merrow Ratings - 2014 Kestrel Protection Honours for Term Cover
• Trusafe has been awarded - Merrow Ratings - 2015 Kestrel Protection Honours for Term Cover

```html
<!DOCTYPE html>
<html lang="en">
<head>
<meta charset="utf-8">
<title>Gardowell – For the price of a coffee</title>
<link rel="stylesheet" href="https://fonts.googleapis.com/css2?family=Roboto:wght@400;700;900&family=Merriweather:wght@400&family=Open+Sans:wght@400;700&display=swap">
<style>
  :root {
    --brand-blue: #1f45a8;
    --brand-green: #8dc63f;
    --green-light: #8fe04a;
    --green-deep: #2fa52a;
    --coffee-dark: #3a2416;
    --coffee-mid: #6e4529;
    --texture-light: #a98a6c;
    --texture-dark: #5e4330;
    --white: #ffffff;
    --ink: #1a1a1a;
  }
  * { box-sizing: border-box; margin: 0; padding: 0; }
  html, body { width: 1200px; height: 566px; overflow: hidden; background: #ffffff; }
  .flyer { position: relative; width: 1200px; height: 566px; overflow: hidden; font-family: "Open Sans", sans-serif; }

  .hero {
    position: absolute; left: 0; top: 0; width: 601px; height: 522px;
    background: linear-gradient(135deg, var(--green-light) 0%, #55c93a 45%, var(--green-deep) 100%);
  }
  .hero-photo {
    position: absolute; left: 0; top: 0; width: 601px; height: 522px;
    background: linear-gradient(160deg, var(--coffee-mid) 0%, #5a3720 50%, var(--coffee-dark) 100%);
    clip-path: polygon(0 290px, 335px 290px, 335px 195px, 601px 195px, 601px 522px, 0 522px);
  }
  .headline {
    position: absolute; left: 12px; top: 40px;
    font-family: "Roboto", sans-serif; font-weight: 900;
    font-size: 80px; line-height: 72px; letter-spacing: 2px;
    color: var(--white); text-transform: uppercase; white-space: nowrap;
  }
  .subline {
    position: absolute; left: 14px; top: 208px; width: 315px;
    font-family: "Merriweather", serif; font-size: 19px; line-height: 27px;
    color: var(--white);
  }

  .story {
    position: absolute; left: 601px; top: 0; width: 599px; height: 522px;
    background: radial-gradient(ellipse at 40% 35%, var(--texture-light) 0%, #8a6b50 55%, var(--texture-dark) 100%);
  }
  .story-copy {
    position: absolute; left: 630px; top: 14px; width: 556px;
    font-size: 16.6px; line-height: 22.7px; color: var(--white);
  }

  .awards {
    position: absolute; left: 620px; top: 424px; width: 456px; height: 74px;
    background: var(--white); padding: 6px 8px;
    font-size: 12px; line-height: 16px; color: var(--ink);
  }
  .awards li { list-style: none; padding-left: 10px; text-indent: -10px; margin-bottom: 2px; }
  .awards b { font-weight: 700; }
  .award-badge {
    position: absolute; left: 1079px; top: 393px; width: 110px; height: 120px;
    background: var(--white);
  }

  .footer { position: absolute; left: 0; top: 522px; width: 1200px; height: 44px; }
  .footer svg { position: absolute; left: 0; top: 0; }
  .footer-logo {
    position: absolute; left: 67px; top: 4px; width: 166px; height: 36px;
    background: var(--white); display: flex; align-items: center; gap: 6px; padding-left: 8px;
    font-weight: 700; font-size: 16px; color: var(--brand-blue);
  }
  .footer-logo .mark { width: 14px; height: 14px; background: var(--brand-green); flex: none; }
  .footer-company, .footer-licence {
    position: absolute; top: 11px; font-size: 16px; color: var(--white);
  }
  .footer-company { left: 663px; }
  .footer-licence { left: 860px; }
</style>
</head>
<body>
<main class="flyer">
  <section class="hero">
    <div class="hero-photo" role="img" aria-label="Photo of a cup of black coffee on a saucer surrounded by coffee beans on a wooden table"></div>
    <h1 class="headline">For the price<br>of a coffee</h1>
    <p class="subline">you can ensure you and your family get the right start.</p>
  </section>

  <section class="story" role="img" aria-label="Warm brown paper texture with a faint coffee ring stain"></section>
  <div class="story-copy">
    <p>"It doesn't sound like much, but when it comes to life insurance, $1 a day* can make a huge difference if you were to die.</p>
    <p>- For the cost of a cup of coffee a day, you can ensure your family will be left with enough to protect the home, pay for ongoing living expenses and fund your children's continued education.</p>
    <p>- Your life is important</p>
    <p>- Apply today and get 1 month free cover</p>
    <p>- Build your tomorrow</p>
    <p>- company logo gardowell.com.au make prominant</p>
    <p>- *For a monthly premium of $25.33, a 35 year old non-smoking male can obtain $300,000 of term life cover.</p>
    <p>- Example for illustration purpose only. The premium cited is current as at February 2016, is based on the factors referred to in the example and subject to underwriting. You should consider whether this product is appropriate for you. Refer to the Product Disclosure Statement, available from gardowell before deciding whether to acquire the product."</p>
  </div>

  <ul class="awards">
    <li>- <b>Trusafe</b> has been awarded - <b>Merrow Ratings - 2014 Kestrel Protection Honours for Term Cover</b></li>
    <li>- <b>Trusafe</b> has been awarded - <b>Merrow Ratings - 2015 Kestrel Protection Honours for Term Cover</b></li>
  </ul>
  <div class="award-badge" role="img" aria-label="Award badge"></div>

  <footer class="footer">
    <svg width="1200" height="44" viewBox="0 0 1200 44" aria-hidden="true">
      <rect x="0" y="0" width="1200" height="44" fill="var(--brand-green)"/>
      <polygon points="612,0 1200,0 1200,44 588,44" fill="var(--brand-blue)"/>
    </svg>
    <div class="footer-logo"><span class="mark"></span>gardowell.com.au</div>
    <span class="footer-company">Gardowell Pty Ltd</span>
    <span class="footer-licence">ABN 47 253 918 604 AFS Licence 729140</span>
  </footer>
</main>
</body>
</html>
```